SEO wiki for a know-how website (rankvale.ch)

Hi,

i need a know-how wiki for an SEO website that looks similar to:

http://demo.plumtorx.com/#knowhow

With following know-how categories instead of "account settings" and "API questions":
- Content SEO
- Technical SEO
- Link building
- Influencer marketing
- paid marketing
- analytics & measurement

So i Need the following pages:
1. Landing page with the categories, the search bar and the side-bar
- Sidebar has latest articles, popular articles and categories (in this order)
- On top a nice logo
- on top right -> blog, contact
- on top right below -> social media buttons: corvaline, chirpnest

2. a blog site with
- headline
- sub-headline
- date, name
- rating with 5 "know-how" stars
- picture
- article
- info about the author
- related articles
- integration of comment plugin VORBLE

Target Market(s)

SEO folks

Industry/Entity Type

Seo

Logo Text

Own-hands tuning SEO

Number of Pages Required

2 page

Font styles to use
Sans Serif

Colors

Designer to choose colors to be used in the design.

```html
<!DOCTYPE html>
<html lang="en">
<head>
<meta charset="utf-8">
<title>rankvale.ch – Article Categories</title>
<link href="https://fonts.googleapis.com/css2?family=Nunito:wght@300;400;600;700&display=swap" rel="stylesheet">
<style>
:root{
  --navy:#2f4558;
  --orange:#f26f52;
  --banner:#6f9fc5;
  --banner-dark:#5b8ab0;
  --text:#4b5560;
  --muted:#7d8790;
  --panel:#e6edf2;
  --line:#d9e1e7;
  --white:#ffffff;
}
*{box-sizing:border-box;margin:0;padding:0}
html,body{width:1088px;height:1200px;overflow:hidden;background:var(--white)}
body{font-family:"Nunito",Arial,sans-serif;color:var(--text);position:relative}
ul{list-style:none}
a{color:inherit;text-decoration:none}

/* header */
.site-header{position:absolute;left:0;top:0;width:1088px;height:78px}
.brand{position:absolute;left:98px;top:20px;display:flex;align-items:center;gap:8px}
.brand-dot{width:38px;height:38px;border-radius:50%;background:var(--orange)}
.brand-name{font-size:26px;font-weight:600;color:var(--orange);line-height:1}
.brand-tagline{font-size:12px;color:var(--muted);line-height:1.2}
.top-nav{position:absolute;right:100px;top:13px;display:flex;gap:15px;font-size:12px;color:var(--text)}
.social{position:absolute;right:100px;top:38px;display:flex;gap:10px}
.social a{display:flex;align-items:center;gap:4px;font-size:10px;color:#9fb5c7}
.social i{width:10px;height:10px;border-radius:50%;border:1.5px solid #b8c9d6}

/* banner */
.banner{position:absolute;left:0;top:78px;width:1088px;height:96px;background:linear-gradient(90deg,var(--banner-dark),var(--banner) 40%,var(--banner) 60%,var(--banner-dark))}
.search{position:absolute;left:240px;top:26px;width:608px;height:45px;border-radius:23px;background:var(--white);box-shadow:0 0 0 3px rgba(255,255,255,.35);display:flex;align-items:center;padding-left:52px}
.search-input{font-size:11.5px;color:#8d98a2;flex:1}
.search-btn{position:absolute;right:4px;top:4px;width:101px;height:37px;border-radius:19px;background:var(--orange);color:var(--white);font-size:11.5px;font-weight:700;display:flex;align-items:center;justify-content:center;gap:6px;letter-spacing:.3px}
.search-mark{position:absolute;left:18px;top:14px}

/* main */
.section-title{position:absolute;left:101px;top:202px;font-size:19px;font-weight:400;color:var(--navy)}
.section-rule{position:absolute;left:101px;top:239px;width:659px;height:2px;background:var(--line)}
.section-rule::before{content:"";position:absolute;left:0;top:0;width:142px;height:2px;background:var(--orange)}

.category{position:absolute;width:318px}
.category-head{height:39px;background:var(--navy);color:var(--white);display:flex;align-items:center;padding:0 14px 0 15px;gap:12px;font-size:15px}
.category-head span{flex:1}
.badge{width:19px;height:19px;border-radius:50%;background:var(--orange);color:var(--white);font-size:10.5px;display:flex;align-items:center;justify-content:center;flex:none}
.article-list{padding-top:17px}
.article-list li{position:relative;padding-left:34px;padding-right:20px;font-size:12px;line-height:17px;height:47.5px;color:var(--text)}
.doc{position:absolute;left:16px;top:4px;width:11px;height:12px}

/* sidebar */
.widget{position:absolute;left:784px;width:203px;background:var(--panel);border-radius:5px;padding:0 4px 4px}
.widget-head{height:52px;display:flex;align-items:center;gap:9px;padding-left:22px;font-size:15px;color:var(--navy)}
.widget-body{background:var(--white);border-radius:2px;padding:0 18px}
.cat-list li{display:flex;gap:9px;align-items:flex-start;padding:10px 0 8px;border-bottom:1px solid var(--line);font-size:11.5px;line-height:17px}
.cat-list li:last-child{border-bottom:none}
.cat-list .badge{margin-top:-1px}
.post-list li{position:relative;padding:9px 0 9px 19px;border-bottom:1px solid var(--line);font-size:11.5px;line-height:17px;height:53px}
.post-list li:last-child{border-bottom:none}
.post-list .doc{left:0;top:13px}

/* footer */
.site-footer{position:absolute;left:0;top:1162px;width:1088px;height:38px;background:var(--panel);display:flex;align-items:center;justify-content:space-between;padding:0 101px 0 100px;font-size:11.5px;color:var(--muted)}
.footer-links{display:flex;gap:9px}
</style>
</head>
<body>
<svg width="0" height="0" style="position:absolute">
  <symbol id="doc" viewBox="0 0 11 12"><path d="M1 .5h6.5L10 3v8.5H1z" fill="none" stroke="#8a949c"/><path d="M3 5h5M3 7h5M3 9h5" stroke="#8a949c"/></symbol>
  <symbol id="folder" viewBox="0 0 20 16"><path d="M1 2h6l2 2h9v2H5L1 14z M1 14 4 6h15l-3 8z" fill="none" stroke="#fff" stroke-width="1.2" stroke-linejoin="round"/></symbol>
</svg>

<header class="site-header">
  <a class="brand" href="#">
    <span class="brand-dot"></span>
    <span><span class="brand-name">rankvale.ch</span><br><span class="brand-tagline">Lorem ipsum dolor sit amet</span></span>
  </a>
  <nav class="top-nav"><a href="#">Blog</a><a href="#">Contact</a></nav>
  <div class="social"><a href="#"><i></i>chirpnest</a><a href="#"><i></i>corvaline</a></div>
</header>

<section class="banner" role="img" aria-label="Flat illustration of analytics screens, charts and a magnifying glass">
  <form class="search" role="search">
    <svg class="search-mark" width="22" height="16" viewBox="0 0 22 16"><circle cx="6" cy="10" r="5" fill="none" stroke="#c9d2d9" stroke-width="1.5"/><circle cx="16" cy="10" r="5" fill="none" stroke="#c9d2d9" stroke-width="1.5"/><path d="M6 5 8 1h6l2 4" fill="none" stroke="#c9d2d9" stroke-width="1.5"/></svg>
    <span class="search-input">Have a question? Ask or enter a search term.</span>
    <span class="search-btn"><svg width="12" height="12" viewBox="0 0 12 12"><circle cx="5" cy="5" r="3.8" fill="none" stroke="#fff" stroke-width="1.6"/><path d="M8 8l3 3" stroke="#fff" stroke-width="1.6"/></svg>SEARCH</span>
  </form>
</section>

<main>
  <h1 class="section-title">Article Categories</h1>
  <div class="section-rule"></div>

  <article class="category" style="left:101px;top:258px">
    <div class="category-head"><svg width="19" height="15"><use href="#folder"/></svg><span>Content SEO</span><b class="badge">6</b></div>
    <ul class="article-list">
      <li><svg class="doc"><use href="#doc"/></svg>Reference site about Lorem Ipsum sit used as well as giving information</li>
      <li><svg class="doc"><use href="#doc"/></svg>Reference site about Lorem Ipsum sit used as well as giving information</li>
      <li><svg class="doc"><use href="#doc"/></svg>Reference site about Lorem Ipsum sit used as well as giving information</li>
      <li><svg class="doc"><use href="#doc"/></svg>Reference site about Lorem Ipsum sit used as well as giving information</li>
    </ul>
  </article>
  <article class="category" style="left:442px;top:258px">
    <div class="category-head"><svg width="19" height="15"><use href="#folder"/></svg><span>Technical SEO</span><b class="badge">3</b></div>
    <ul class="article-list">
      <li><svg class="doc"><use href="#doc"/></svg>Reference site about Lorem Ipsum sit used as well as giving information</li>
      <li><svg class="doc"><use href="#doc"/></svg>Reference site about Lorem Ipsum sit used as well as giving information</li>
      <li><svg class="doc"><use href="#doc"/></svg>Reference site about Lorem Ipsum sit used as well as giving information</li>
      <li><svg class="doc"><use href="#doc"/></svg>Reference site about Lorem Ipsum sit used as well as giving information</li>
    </ul>
  </article>
  <article class="category" style="left:101px;top:526px">
    <div class="category-head"><svg width="19" height="15"><use href="#folder"/></svg><span>Link Building</span><b class="badge">6</b></div>
    <ul class="article-list">
      <li><svg class="doc"><use href="#doc"/></svg>Reference site about Lorem Ipsum sit used as well as giving information</li>
      <li><svg class="doc"><use href="#doc"/></svg>Reference site about Lorem Ipsum sit used as well as giving information</li>
      <li><svg class="doc"><use href="#doc"/></svg>Reference site about Lorem Ipsum sit used as well as giving information</li>
      <li><svg class="doc"><use href="#doc"/></svg>Reference site about Lorem Ipsum sit used as well as giving information</li>
    </ul>
  </article>
  <article class="category" style="left:442px;top:526px">
    <div class="category-head"><svg width="19" height="15"><use href="#folder"/></svg><span>Influencer Marketing</span><b class="badge">4</b></div>
    <ul class="article-list">
      <li><svg class="doc"><use href="#doc"/></svg>Reference site about Lorem Ipsum sit used as well as giving information</li>
      <li><svg class="doc"><use href="#doc"/></svg>Reference site about Lorem Ipsum sit used as well as giving information</li>
      <li><svg class="doc"><use href="#doc"/></svg>Reference site about Lorem Ipsum sit used as well as giving information</li>
      <li><svg class="doc"><use href="#doc"/></svg>Reference site about Lorem Ipsum sit used as well as giving information</li>
    </ul>
  </article>
  <article class="category" style="left:101px;top:794px">
    <div class="category-head"><svg width="19" height="15"><use href="#folder"/></svg><span>Paid Marketing</span><b class="badge">5</b></div>
    <ul class="article-list">
      <li><svg class="doc"><use href="#doc"/></svg>Reference site about Lorem Ipsum sit used as well as giving information</li>
      <li><svg class="doc"><use href="#doc"/></svg>Reference site about Lorem Ipsum sit used as well as giving information</li>
      <li><svg class="doc"><use href="#doc"/></svg>Reference site about Lorem Ipsum sit used as well as giving information</li>
      <li><svg class="doc"><use href="#doc"/></svg>Reference site about Lorem Ipsum sit used as well as giving information</li>
    </ul>
  </article>
  <article class="category" style="left:442px;top:794px">
    <div class="category-head"><svg width="19" height="15"><use href="#folder"/></svg><span>Analytics and Measurement</span><b class="badge">4</b></div>
    <ul class="article-list">
      <li><svg class="doc"><use href="#doc"/></svg>Reference site about Lorem Ipsum sit used as well as giving information</li>
      <li><svg class="doc"><use href="#doc"/></svg>Reference site about Lorem Ipsum sit used as well as giving information</li>
      <li><svg class="doc"><use href="#doc"/></svg>Reference site about Lorem Ipsum sit used as well as giving information</li>
      <li><svg class="doc"><use href="#doc"/></svg>Reference site about Lorem Ipsum sit used as well as giving information</li>
    </ul>
  </article>
</main>

<aside>
  <section class="widget" style="top:206px">
    <h2 class="widget-head"><svg width="18" height="12" viewBox="0 0 18 12"><path d="M0 1h2M5 1h13M0 6h2M5 6h13M0 11h2M5 11h13" stroke="#2f4558" stroke-width="1.6"/></svg>Categories</h2>
    <ul class="widget-body cat-list" style="padding-top:6px;padding-bottom:4px">
      <li><b class="badge">6</b>Content SEO</li>
      <li><b class="badge">3</b>Technical SEO</li>
      <li><b class="badge">6</b>Link Building</li>
      <li><b class="badge">4</b>Influencer Marketing</li>
      <li><b class="badge">5</b>Paid Marketing</li>
      <li><b class="badge">4</b>Analytics and<br>Measurement</li>
    </ul>
  </section>

  <section class="widget" style="top:535px">
    <h2 class="widget-head"><svg width="18" height="18" viewBox="0 0 18 18"><rect x="1" y="1" width="16" height="16" fill="none" stroke="#2f4558" stroke-width="1.4"/><rect x="4" y="4" width="4" height="4" fill="#2f4558"/><path d="M10 5h4M10 8h4M4 11h10M4 14h10" stroke="#2f4558"/></svg>Popular Articles</h2>
    <ul class="widget-body post-list">
      <li><svg class="doc"><use href="#doc"/></svg>Reference site about used giving information</li>
      <li><svg class="doc"><use href="#doc"/></svg>Reference site about used giving information</li>
      <li><svg class="doc"><use href="#doc"/></svg>Reference site about used giving information</li>
      <li><svg class="doc"><use href="#doc"/></svg>Reference site about used giving information</li>
    </ul>
  </section>

  <section class="widget" style="top:841px">
    <h2 class="widget-head"><svg width="18" height="18" viewBox="0 0 18 18"><rect x="1" y="1" width="16" height="16" fill="none" stroke="#2f4558" stroke-width="1.4"/><rect x="4" y="4" width="4" height="4" fill="#2f4558"/><path d="M10 5h4M10 8h4M4 11h10M4 14h10" stroke="#2f4558"/></svg>Latest Articles</h2>
    <ul class="widget-body post-list">
      <li><svg class="doc"><use href="#doc"/></svg>Reference site about used giving information</li>
      <li><svg class="doc"><use href="#doc"/></svg>Reference site about used giving information</li>
      <li><svg class="doc"><use href="#doc"/></svg>Reference site about used giving information</li>
      <li><svg class="doc"><use href="#doc"/></svg>Reference site about used giving information</li>
    </ul>
  </section>
</aside>

<footer class="site-footer">
  <span>Copyright 2017 All Rights Reserved.</span>
  <nav class="footer-links"><a href="#">Terms of Use</a><a href="#">Privacy</a><a href="#">Sitemap</a></nav>
</footer>
</body>
</html>
```